Business Card Design

Need a hot business card in wine colors something cool and mod please feel free to be , FUNKY and free with this .

Industry/Entity Type

Business

Contact Information for Business Card

LUMERA HAIR DESIGN 3182 W 9th St Scottsdale AZ 85619 Custom modern hair design and custom color by MARCUS OBRIDGE 602-4168203 cell salon 480 -712-6084 email marcusobridge@quillpost.com hours wed thru sat 7am to 6pm.

Font styles to use
Other font styles liked:
• something fun and mod.

Colors
a54599
6b449b
1b1b1b
606060

Requirements
Must have
• Apointment reminder on flip side of card.
Should not have
• Nothing boring.

```html
<!DOCTYPE html>
<html lang="en">
<head>
<meta charset="utf-8">
<title>Lumera Hair Design – Business Card</title>
<link rel="stylesheet" href="https://fonts.googleapis.com/css2?family=Open+Sans:wght@400;600;700&family=Great+Vibes&family=Dancing+Script:wght@500&display=swap">
<style>
  :root{
    --wine:#a54599;
    --violet:#6b449b;
    --violet-light:#8d62c4;
    --lilac:#9a72cf;
    --ink:#1b1b1b;
    --grey:#606060;
    --paper:#ffffff;
    --backdrop:#e9e6ec;
  }
  *{margin:0;padding:0;box-sizing:border-box}
  html,body{width:1200px;height:1023px;overflow:hidden}
  body{background:var(--backdrop);font-family:"Open Sans",Arial,sans-serif;position:relative}

  .card{position:absolute;width:700px;height:400px;border-radius:24px;overflow:hidden;background:var(--paper);box-shadow:0 10px 30px rgba(27,27,27,.18)}
  .card--reminder{left:90px;top:60px}
  .card--contact{left:410px;top:560px}
  .card__wave{position:absolute;inset:0;width:100%;height:100%}

  .brand{position:absolute;display:flex;align-items:center;gap:14px}
  .brand__square{width:74px;height:66px;border-radius:8px;background:var(--violet)}
  .brand__name{color:var(--violet);line-height:1.05}
  .brand__word{display:block;font-weight:600;font-size:31px;letter-spacing:.5px}
  .brand__sub{display:block;font-weight:400;font-size:24px;letter-spacing:1.5px}
  .divider{position:absolute;width:2px;background:#d3cbdc}

  /* contact side */
  .card--contact .brand{left:76px;top:74px}
  .card--contact .divider{left:364px;top:68px;height:82px}
  .tagline{position:absolute;left:392px;top:74px;color:var(--violet-light);font-size:20px;line-height:32px}
  .holder{position:absolute;left:66px;top:262px;font-family:"Great Vibes",cursive;color:var(--paper);font-size:46px}
  .contact-list{position:absolute;left:430px;top:224px;list-style:none;color:var(--paper);font-size:16.5px;line-height:23px}
  .contact-list li{display:flex;align-items:flex-start;gap:10px}
  .contact-list li.address{margin-top:8px}
  .contact-list svg{width:14px;height:14px;margin-top:4px;flex:none;fill:var(--paper)}

  /* reminder side */
  .card--reminder .brand{left:42px;top:48px}
  .card--reminder .divider{left:330px;top:40px;height:80px}
  .reminder-title{position:absolute;left:352px;top:44px;font-family:"Dancing Script",cursive;color:var(--wine);font-size:31px}
  .hours{position:absolute;left:0;width:700px;top:128px;text-align:center;color:var(--wine);font-size:14.5px;line-height:22px}
  .hours strong{font-weight:700}
  .slot{position:absolute;display:flex;align-items:flex-end;color:var(--paper);font-size:17px}
  .slot__line{flex:1;border-bottom:1.5px dotted rgba(255,255,255,.75);margin-left:6px;height:18px}
  .slot--date{left:40px;width:400px}
  .slot--time{left:448px;width:220px}
</style>
</head>
<body>

<section class="card card--reminder" aria-label="Appointment reminder side">
  <svg class="card__wave" viewBox="0 0 700 400" preserveAspectRatio="none" aria-hidden="true">
    <defs>
      <linearGradient id="waveBack" x1="0" y1="0" x2="1" y2="1">
        <stop offset="0" stop-color="#6b449b"/>
        <stop offset=".55" stop-color="#8a5fc2"/>
        <stop offset="1" stop-color="#6b449b"/>
      </linearGradient>
    </defs>
    <path d="M0 208 C200 222 450 204 700 166 L700 400 L0 400Z" fill="#a54599"/>
    <path d="M0 217 C200 231 450 213 700 176 L700 400 L0 400Z" fill="url(#waveBack)"/>
  </svg>
  <div class="brand">
    <span class="brand__square"></span>
    <span class="brand__name"><span class="brand__word">LUMERA</span><span class="brand__sub">Hair Design</span></span>
  </div>
  <span class="divider"></span>
  <p class="reminder-title">Your Next Appointment</p>
  <p class="hours"><strong>Openning Hours:</strong><br>Wednesday to Saturday ........ 7:00am to 6:00pm</p>

  <div class="slot slot--time" style="top:208px">Time:<span class="slot__line"></span></div>
  <div class="slot slot--time" style="top:242px">Time:<span class="slot__line"></span></div>
  <div class="slot slot--time" style="top:276px">Time:<span class="slot__line"></span></div>
  <div class="slot slot--time" style="top:310px">Time:<span class="slot__line"></span></div>

  <div class="slot slot--date" style="top:248px">Date:<span class="slot__line"></span></div>
  <div class="slot slot--date" style="top:282px">Date:<span class="slot__line"></span></div>
  <div class="slot slot--date" style="top:316px">Date:<span class="slot__line"></span></div>
  <div class="slot slot--date" style="top:350px">Date:<span class="slot__line"></span></div>
</section>

<section class="card card--contact" aria-label="Contact side">
  <svg class="card__wave" viewBox="0 0 700 400" preserveAspectRatio="none" aria-hidden="true">
    <defs>
      <linearGradient id="waveFront" x1="0" y1="0" x2="1" y2="1">
        <stop offset="0" stop-color="#6b449b"/>
        <stop offset=".55" stop-color="#9a72cf"/>
        <stop offset="1" stop-color="#6b449b"/>
      </linearGradient>
    </defs>
    <path d="M0 170 C120 200 220 225 350 200 C470 178 560 160 700 235 L700 400 L0 400Z" fill="#a54599"/>
    <path d="M0 182 C120 212 220 236 350 212 C470 190 570 174 700 246 L700 400 L0 400Z" fill="url(#waveFront)"/>
  </svg>
  <div class="brand">
    <span class="brand__square"></span>
    <span class="brand__name"><span class="brand__word">LUMERA</span><span class="brand__sub">Hair Design</span></span>
  </div>
  <span class="divider"></span>
  <p class="tagline">Custom Modern Hair Design<br>and Custom Color</p>
  <p class="holder">Marcus Obridge</p>
  <ul class="contact-list">
    <li><svg viewBox="0 0 14 14"><rect x="3.5" y="0" width="7" height="14" rx="1.5"/><rect x="5" y="1.8" width="4" height="8.5" fill="#8a5fc2"/></svg>602-416-8203</li>
    <li><svg viewBox="0 0 14 14"><path d="M1 5 C1 2 13 2 13 5 L10 6 L9 4.5 H5 L4 6Z"/><rect x="2" y="7" width="10" height="6" rx="1"/></svg>480-712-6084</li>
    <li><svg viewBox="0 0 14 14"><path d="M1 3 H13 V11 H1Z"/><path d="M1 3 L7 8 L13 3" fill="none" stroke="#8a5fc2" stroke-width="1.2"/></svg>marcusobridge@quillpost.com</li>
    <li class="address"><svg viewBox="0 0 14 14"><path d="M7 0 C3.5 0 2 2.5 2 5 C2 8.5 7 14 7 14 C7 14 12 8.5 12 5 C12 2.5 10.5 0 7 0Z"/><circle cx="7" cy="5" r="2" fill="#8a5fc2"/></svg>3182 W 9th St Scottsdale<br>AZ 85619</li>
  </ul>
</section>

</body>
</html>
```